Quillory Nest Business Card

I need a business card design. We are a collaborate online training company. Our colors are gray and green. Our website is QuilloryNest.com

I would like an area for a profile picture within the card

```html
<!DOCTYPE html>
<html lang="en">
<head>
<meta charset="utf-8">
<title>Quillory Nest Business Card</title>
<link rel="stylesheet" href="https://fonts.googleapis.com/css2?family=Open+Sans:wght@400;600;700&display=swap">
<style>
  :root {
    --green: #8cc63f;
    --ink: #1c1c1c;
    --card-white: #ffffff;
    --card-black: #050607;
    --backdrop: #6b6b6b;
    --photo-dark: #3a3d42;
    --photo-light: #c9b8aa;
  }
  html, body {
    margin: 0;
    padding: 0;
    width: 1200px;
    height: 1200px;
    overflow: hidden;
    background: var(--backdrop);
    font-family: "Open Sans", Arial, sans-serif;
  }
  .card {
    position: absolute;
    left: 273px;
    width: 655px;
    height: 371px;
    box-shadow: 0 4px 10px rgba(0,0,0,0.45);
    overflow: hidden;
  }
  .card-front { top: 197px; background: var(--card-white); }
  .card-back { top: 633px; background: var(--card-black); }

  .profile-photo {
    position: absolute;
    left: 0;
    top: 30px;
    width: 252px;
    height: 341px;
    background: linear-gradient(160deg, var(--photo-light) 0%, #a88f7f 40%, var(--photo-dark) 100%);
  }

  .brand {
    position: absolute;
    display: flex;
    align-items: center;
    gap: 10px;
    font-weight: 700;
    font-size: 36px;
    letter-spacing: -0.5px;
    white-space: nowrap;
  }
  .brand-dot {
    width: 40px;
    height: 40px;
    border-radius: 50%;
    background: var(--green);
    flex: none;
  }
  .card-front .brand { left: 323px; top: 56px; color: var(--ink); }
  .card-back .brand { left: 50%; top: 142px; transform: translateX(-50%); color: #ffffff; }

  .holder-name {
    position: absolute;
    left: 323px;
    top: 168px;
    margin: 0;
    font-size: 24px;
    font-weight: 400;
    color: var(--ink);
  }
  .name-rule {
    position: absolute;
    left: 323px;
    top: 207px;
    width: 303px;
    height: 1.5px;
    background: var(--green);
  }
  .contact-list {
    position: absolute;
    left: 323px;
    top: 224px;
    margin: 0;
    padding: 0;
    list-style: none;
    font-size: 16px;
    line-height: 22px;
    color: var(--ink);
  }
  .contact-list li { display: flex; align-items: center; gap: 8px; }
  .contact-list svg { width: 18px; height: 16px; flex: none; }
  .address {
    position: absolute;
    left: 323px;
    top: 302px;
    margin: 0;
    font-style: normal;
    font-size: 16px;
    line-height: 22px;
    color: var(--ink);
  }
  .back-url {
    position: absolute;
    left: 0;
    right: 0;
    top: 331px;
    text-align: center;
    color: #ffffff;
    font-size: 16px;
  }
</style>
</head>
<body>
  <section class="card card-front">
    <div class="profile-photo" role="img" aria-label="Profile portrait of the card holder in a dark suit"></div>
    <div class="brand"><span class="brand-dot"></span>QuilloryNest</div>
    <h1 class="holder-name">Dana Whitfield</h1>
    <div class="name-rule"></div>
    <ul class="contact-list">
      <li>
        <svg viewBox="0 0 18 16" aria-hidden="true"><path fill="#8cc63f" d="M1 5c0-2 4-3 8-3s8 1 8 3v2h-4V5.5c-1-.5-3-.7-4-.7s-3 .2-4 .7V7H1zM4 8l2-2h6l2 2v6H4z"/><circle cx="9" cy="11" r="2" fill="#fff"/></svg>
        (555) 013-2847
      </li>
      <li>
        <svg viewBox="0 0 18 16" aria-hidden="true"><rect x="1" y="3" width="16" height="11" fill="#8cc63f"/><path d="M1 3l8 6 8-6" fill="none" stroke="#fff" stroke-width="1.3"/></svg>
        dana@quillorynest.com
      </li>
      <li>
        <svg viewBox="0 0 18 16" aria-hidden="true"><g fill="none" stroke="#8cc63f" stroke-width="1.2"><circle cx="9" cy="8" r="7"/><ellipse cx="9" cy="8" rx="3" ry="7"/><path d="M2 8h14M3 4.5h12M3 11.5h12"/></g></svg>
        www.quillorynest.com
      </li>
    </ul>
    <address class="address">4870 Larkspur Ave. Suite 11<br>Marlow Heights, Oregon 97301</address>
  </section>

  <section class="card card-back">
    <div class="brand"><span class="brand-dot"></span>QuilloryNest</div>
    <div class="back-url">www.quillorynest.com</div>
  </section>
</body>
</html>
```